Australian Software Consultancy needs new Business Card Design

Design Business Card based on existing design artefacts (attached). We are open to all designs. As its a 2 sided design and we thought it might be quite striking to have one side with a black background and te other side with a white background.

Target Market(s)

Financial Services mainly.

Industry/Entity Type

Business

Contact Information for Business Card

Name :
Position :
Email :

Requirements
Must have
• Funky design using our existing assets

```html
<!DOCTYPE html>
<html lang="en">
<head>
<meta charset="utf-8">
<title>Bright Field — Business Card</title>
<link rel="stylesheet" href="https://fonts.googleapis.com/css2?family=Montserrat:wght@500;600;700&display=swap">
<style>
  :root {
    --backdrop: #1c1c1c;
    --brand-red: #e8232a;
    --paper-white: #ffffff;
    --ink-black: #161616;
  }
  * { margin: 0; padding: 0; box-sizing: border-box; }
  html, body {
    width: 1200px;
    height: 1000px;
    overflow: hidden;
    background: var(--backdrop);
    font-family: "Montserrat", sans-serif;
  }
  .canvas {
    position: relative;
    width: 1200px;
    height: 1000px;
  }
  .card {
    position: absolute;
    left: 320px;
    width: 560px;
    height: 320px;
    border-radius: 18px;
    overflow: hidden;
    background: var(--brand-red);
  }
  .card--front { top: 140px; }
  .card--back  { top: 540px; }

  .front-wordmark {
    position: absolute;
    inset: 0;
    display: flex;
    align-items: center;
    justify-content: center;
    color: var(--paper-white);
    font-weight: 700;
    font-size: 44px;
    letter-spacing: 1px;
  }

  .back-art {
    position: absolute;
    inset: 0;
  }
  .back-art .band-black { fill: var(--ink-black); }
  .back-art .band-red   { fill: var(--brand-red); }
  .back-art .panel-white { fill: var(--paper-white); }
  .back-art .brand-ring {
    fill: none;
    stroke: var(--brand-red);
    stroke-width: 10;
  }
  .back-art .brand-name {
    fill: var(--brand-red);
    font-family: "Montserrat", sans-serif;
    font-weight: 700;
    font-size: 19px;
  }

  .contact {
    position: absolute;
    left: 44px;
    top: 178px;
    color: var(--paper-white);
  }
  .contact__name {
    font-weight: 700;
    font-size: 18px;
    letter-spacing: 0.5px;
  }
  .contact__role {
    font-weight: 600;
    font-size: 12px;
    letter-spacing: 0.5px;
    margin: 4px 0 16px 4px;
  }
  .contact__line {
    display: flex;
    align-items: center;
    gap: 10px;
    font-weight: 500;
    font-size: 13px;
    margin: 0 0 6px 8px;
  }
  .contact__icon {
    width: 11px;
    height: 11px;
    fill: var(--paper-white);
  }
</style>
</head>
<body>
<main class="canvas">

  <section class="card card--front" aria-label="Card front">
    <div class="front-wordmark">BRIGHT FIELD</div>
  </section>

  <section class="card card--back" aria-label="Card back">
    <svg class="back-art" viewBox="0 0 560 320" width="560" height="320">
      <path class="band-black" d="M352 0 C268 70 275 250 380 320 L560 320 L560 0 Z"/>
      <path class="band-red" d="M362 0 C282 70 292 250 396 320 L560 320 L560 0 Z"/>
      <path class="panel-white" d="M374 0 C298 70 310 250 410 320 L560 320 L560 0 Z"/>
      <circle class="brand-ring" cx="455" cy="160" r="92"/>
      <text class="brand-name" x="455" y="167" text-anchor="middle">BRIGHT FIELD</text>
    </svg>

    <div class="contact">
      <p class="contact__name">DANIEL REYES</p>
      <p class="contact__role">FOUNDER</p>
      <p class="contact__line">
        <svg class="contact__icon" viewBox="0 0 24 24"><path d="M6.6 10.8a15 15 0 0 0 6.6 6.6l2.2-2.2a1 1 0 0 1 1-.25 11.4 11.4 0 0 0 3.6.57 1 1 0 0 1 1 1V20a1 1 0 0 1-1 1A17 17 0 0 1 3 4a1 1 0 0 1 1-1h3.5a1 1 0 0 1 1 1c0 1.25.2 2.45.57 3.57a1 1 0 0 1-.25 1z"/></svg>
        <span>000 000 0000</span>
      </p>
      <p class="contact__line">
        <svg class="contact__icon" viewBox="0 0 24 24"><path d="M2 5h20v14H2z M2 5l10 8 10-8" fill="none" stroke="#fff" stroke-width="2.5"/></svg>
        <span>info@danielreyes.com</span>
      </p>
    </div>
  </section>

</main>
</body>
</html>
```